Peter Lanford Studios Business Card

Looking for a clear, modern, elegant, sharp business card that conveys a professional yet edgy image to my business as a wedding, portrait, and travel photographer. Would like something that looks vintage yet modern. Need a new business card to grow my business. We are growing the business for Wedding and Event Photography as well as fine art Photography. (Mostly Landscapes)
Updates

I’m looking through designs now but I have a new logo that i want using please.

New logo uploaded please redesign using that

PLEASE ALL DESIGNERS LOOK IN BRIEF FOR NEW LOGO

Target Market(s)

Brides, Grooms, Families with Kids, People looking for Fine Art Photography Artwork

Industry/Entity Type

Photographer

Contact Information for Business Card

Unsure

Font styles to use
Serif

Colors

Designer to choose colors to be used in the design.

Requirements
Must have
• My Website:
• http://lanfordgallery.snapfolio.example
• Phone:
• 555-418-2061
• Email:
• petelanfordgallery@mailbox.example
Nice to have
• Would like a sort of shine on the printing finish.
• I like black I think it looks good on a business card.
• Can try working with my logo (png that I've attached)

```html
<!DOCTYPE html>
<html lang="en">
<head>
<meta charset="utf-8">
<title>Peter Lanford Studios – Business Card</title>
<link href="https://fonts.googleapis.com/css2?family=Questrial&display=swap" rel="stylesheet">
<style>
  :root {
    --backdrop: #3b3b3d;
    --card-dark: #141416;
    --card-mid: #2a2b2e;
    --ink: #f2f2f2;
    --ink-soft: #d9d9d9;
  }
  * { box-sizing: border-box; margin: 0; padding: 0; }
  html, body {
    width: 799px;
    height: 1200px;
    overflow: hidden;
    background: var(--backdrop);
    font-family: "Questrial", "Century Gothic", sans-serif;
    color: var(--ink);
  }
  .sheet {
    position: relative;
    width: 799px;
    height: 1200px;
  }
  .card {
    position: absolute;
    left: 50px;
    width: 700px;
    height: 400px;
    border-radius: 26px;
    background:
      linear-gradient(160deg, rgba(255,255,255,0.06) 0%, rgba(255,255,255,0) 45%),
      linear-gradient(180deg, var(--card-mid) 0%, var(--card-dark) 100%);
    box-shadow: 0 14px 30px rgba(0,0,0,0.45);
    overflow: hidden;
  }
  .card--front { top: 130px; }
  .card--back  { top: 670px; }

  .brand {
    position: absolute;
    display: flex;
    flex-direction: column;
    align-items: center;
    color: var(--ink);
  }
  .brand__mark {
    width: 62px;
    height: 62px;
    border: 2px solid var(--ink);
    margin-bottom: 12px;
  }
  .brand__name {
    font-size: 46px;
    letter-spacing: 1px;
    line-height: 1;
    white-space: nowrap;
  }
  .brand__sub {
    font-size: 17px;
    letter-spacing: 12px;
    margin-top: 8px;
    padding-left: 12px;
  }
  .card--front .brand {
    left: 0;
    right: 0;
    top: 110px;
  }
  .card--back .brand {
    right: 34px;
    bottom: 36px;
  }
  .card--back .brand__mark { width: 52px; height: 52px; margin-bottom: 10px; }
  .card--back .brand__name { font-size: 38px; }
  .card--back .brand__sub { font-size: 14px; letter-spacing: 10px; }

  .holder {
    position: absolute;
    left: 36px;
    top: 34px;
    font-size: 30px;
    color: var(--ink);
  }
  .contacts {
    position: absolute;
    left: 36px;
    bottom: 48px;
    list-style: none;
    font-size: 15px;
    color: var(--ink-soft);
  }
  .contacts__item {
    display: flex;
    align-items: center;
    gap: 10px;
    line-height: 24px;
  }
  .contacts__icon {
    width: 13px;
    height: 13px;
    fill: var(--ink-soft);
    flex: none;
  }
</style>
</head>
<body>
<main class="sheet">
  <section class="card card--front" aria-label="Card front">
    <div class="brand">
      <span class="brand__mark"></span>
      <span class="brand__name">PETER LANFORD</span>
      <span class="brand__sub">STUDIOS</span>
    </div>
  </section>

  <section class="card card--back" aria-label="Card back">
    <p class="holder">Peter Lanford</p>
    <ul class="contacts">
      <li class="contacts__item">
        <svg class="contacts__icon" viewBox="0 0 16 16" aria-hidden="true"><path d="M1 5c0-2 3-3 7-3s7 1 7 3v1h-4V5H5v1H1z"/><path d="M3 8h10l1 6H2z"/></svg>
        555-418-2061
      </li>
      <li class="contacts__item">
        <svg class="contacts__icon" viewBox="0 0 16 16" aria-hidden="true"><path d="M1 3h14v10H1z" fill="none" stroke="#d9d9d9" stroke-width="1.6"/><path d="M1 3l7 6 7-6" fill="none" stroke="#d9d9d9" stroke-width="1.6"/></svg>
        petelanfordgallery@mailbox.example
      </li>
      <li class="contacts__item">
        <svg class="contacts__icon" viewBox="0 0 16 16" aria-hidden="true"><circle cx="8" cy="8" r="6.5" fill="none" stroke="#d9d9d9" stroke-width="1.4"/><ellipse cx="8" cy="8" rx="2.8" ry="6.5" fill="none" stroke="#d9d9d9" stroke-width="1.2"/><path d="M1.5 8h13" stroke="#d9d9d9" stroke-width="1.2"/></svg>
        www.lanfordgallery.snapfolio.example
      </li>
    </ul>
    <div class="brand">
      <span class="brand__mark"></span>
      <span class="brand__name">PETER LANFORD</span>
      <span class="brand__sub">STUDIOS</span>
    </div>
  </section>
</main>
</body>
</html>
```